Regenerative Medicine Brochure

I want a clean modern bi-fold or tri-fold brochure. We offer non-surgical joint repair for knees, shoulders, and hips. We have many services available including regenerative medicine including stem cell allograft, palatelet rich plasma, prolotherapy, triggerpoint injection, chiropractic and rehab therapies. We are a modern multidisciplinary clinic in coastal California. My logo is already complete and is a vibrant green color. I prefer lots of white space with some areas for service description and what conditions may benefit from the services. Design should convey modern treatments, upscale office and practice, and our target audience is older adults who want to maintain an active pain-free lifestyle.

Target Market(s)

Sports injuries, athletes, seniors who are active, knee pain, shoulder pain, arthritis.

Industry/Entity Type

Alternative Medicine

Font styles to use
Serif

Colors
9bcb3c

Requirements
Must have
• Small white space where we can write date, time, location of next event/class. Colors in brochure to coordinate with logo colors provided.

```html
<!DOCTYPE html>
<html lang="en">
<head>
<meta charset="utf-8">
<title>Coastline Spine &amp; Joint – Regenerative Medicine Brochure</title>
<link rel="stylesheet" href="https://fonts.googleapis.com/css2?family=Source+Sans+3:wght@400;600&family=Tinos:wght@400;700&display=swap">
<style>
  :root{
    --green:#9bcb3c;
    --green-dark:#7fb02a;
    --green-pale:#e6f0d2;
    --charcoal:#3c3c3c;
    --ink:#333;
    --grey-soft:#e4e4e4;
    --paper:#ffffff;
    --bg:#d9d5cf;
  }
  *{box-sizing:border-box;margin:0;padding:0}
  html,body{width:1200px;height:1200px;overflow:hidden;background:var(--bg)}
  body{position:relative;font-family:"Tinos",serif;color:var(--ink)}
  .spread{position:absolute;left:150px;width:900px;height:560px;display:flex;background:var(--paper);box-shadow:0 2px 8px rgba(0,0,0,.15)}
  .spread--outside{top:30px}
  .spread--inside{top:610px}
  .panel{position:relative;width:300px;height:100%;overflow:hidden;padding:26px 20px 0}
  .panel + .panel{border-left:1px solid #ececec}
  .heading{font-family:"Source Sans 3",sans-serif;font-weight:600;color:var(--green-dark);font-size:12.5px;line-height:1.25;margin-bottom:12px}
  .body-copy{font-size:8.4px;line-height:1.32;text-align:justify;margin-bottom:9px}
  .photo{position:absolute;left:0;right:0;bottom:0;height:190px}
  .photo--knee{background:linear-gradient(to bottom,rgba(255,255,255,1) 0%,rgba(190,185,175,.9) 35%,#8f8a80 100%)}
  .photo--hands{background:linear-gradient(to bottom,#fff 0%,#e9d7cd 35%,#c9ada0 100%)}
  .photo--back{background:linear-gradient(to bottom,#fff 0%,#d8d4cc 35%,#a7a79a 100%)}
  .photo--patient{position:absolute;left:0;right:0;top:80px;height:330px;background:linear-gradient(to bottom,#e4e4e4,#d4c4c8 50%,#c9a0ad)}
  .event-fields{margin-top:70px;font-family:"Source Sans 3",sans-serif;font-size:9px;font-weight:600;color:var(--charcoal)}
  .event-fields div{display:flex;align-items:flex-end;margin-bottom:11px}
  .event-fields span{flex:1;border-bottom:1px solid #888;margin-left:6px;height:1px}
  .brand{display:flex;align-items:center;gap:7px;font-family:"Source Sans 3",sans-serif;font-weight:400;color:var(--charcoal)}
  .brand__dot{width:8px;height:8px;background:var(--green)}
  .brand--small{font-size:15px;margin-top:60px}
  .brand--cover{font-size:17px;justify-content:center}
  .contact{list-style:none;margin-top:18px;font-size:7.6px;line-height:1.35}
  .contact li{display:flex;gap:6px;margin-bottom:6px;align-items:flex-start}
  .contact svg{width:8px;height:8px;flex:none;margin-top:1px}
  .swoop{position:absolute;left:0;bottom:0;width:300px;height:110px}
  .cover-band{position:absolute;left:0;bottom:0;width:300px;height:160px}
  .cover-title{position:absolute;left:0;right:0;bottom:48px;text-align:center;font-family:"Source Sans 3",sans-serif;font-weight:600;color:#fff;font-size:19px;line-height:1.15;letter-spacing:.2px}
  .cover-url{position:absolute;left:0;right:0;bottom:14px;text-align:center;color:#fff;font-size:7.5px}
  .panel--areas{background:linear-gradient(to bottom,var(--green-pale),#f5f9ec 70%,#fff)}
  .areas-intro{font-family:"Source Sans 3",sans-serif;font-weight:600;font-size:8.5px;margin-bottom:10px}
  .figure{position:absolute;left:120px;top:60px;width:150px;height:300px;background:linear-gradient(#6b6b6b,#4a4a4a);border-radius:70px 70px 40px 40px;opacity:.85}
  .area-label{position:absolute;left:40px;font-family:"Source Sans 3",sans-serif;font-size:9.5px;color:var(--charcoal)}
  .area-label::after{content:"";position:absolute;left:48px;top:6px;width:var(--len);border-top:1px solid #999}
  .areas-copy{position:absolute;left:20px;right:20px;top:385px}
</style>
</head>
<body>

<section class="spread spread--outside">
  <article class="panel">
    <h2 class="heading">What can I expect from regenerative medicine treatments?</h2>
    <p class="body-copy">During your visit, the team begins with a consultation and physical exam to determine if you're a candidate for regenerative medicine. They ask about your symptoms, condition, overall health, and lifestyle. If you're a candidate, the team then explains the procedure and what to expect both during and afterward.</p>
    <p class="body-copy">For the procedure, the team first cleans your skin and, if needed, applies a topical numbing cream to your skin. Next, the team injects regenerative products into the treatment area. You may feel a slight pinch or burning sensation during the injection. The injection takes less than five minutes and you can return to your usual activities the same day. Mild soreness at the injection site is possible for two to three days.</p>
    <p class="body-copy">Over the coming weeks and months, the injected products help repair damaged tissues at the treatment site. Most people notice results after two months. Follow-up care may be recommended based on your condition and initial results. The team has seen dramatic results with regenerative medicine treatments; however, individual results can vary. Speak to the team to see if regenerative medicine is right for you.</p>
    <div class="photo photo--knee" role="img" aria-label="Photo of a runner sitting on a path holding an injured knee"></div>
  </article>

  <article class="panel">
    <p class="body-copy">For joint arthritis and muscle pain and injuries, the team at Coastline Spine &amp; Joint offers minimally invasive regenerative medicine techniques to help you recover from chronic pain. Located in Seabright, California, the medical team utilizes advanced restorative techniques to support the natural healing of injured joints and soft tissues without the need for surgery. To learn more, schedule a consultation online or by phone today.</p>
    <div class="event-fields">
      <div>Date:<span></span></div>
      <div>Time:<span></span></div>
      <div>Location:<span></span></div>
    </div>
    <div class="brand brand--small"><i class="brand__dot"></i>Coastline Spine &amp; Joint</div>
    <ul class="contact">
      <li><svg viewBox="0 0 10 10"><path d="M5 0a3.5 3.5 0 0 0-3.5 3.5C1.5 6 5 10 5 10s3.5-4 3.5-6.5A3.5 3.5 0 0 0 5 0z" fill="#9bcb3c"/></svg>2480 Harbor Lane<br>Seabright, CA 93001</li>
      <li><svg viewBox="0 0 10 10"><path d="M2 0l2 2.5-1 1.2a6 6 0 0 0 3.3 3.3l1.2-1L10 8 8.5 10C4 10 0 6 0 1.5z" fill="#9bcb3c"/></svg>555-014-2280</li>
      <li><svg viewBox="0 0 10 10"><rect x="0" y="2" width="10" height="6" fill="#9bcb3c"/><path d="M0 2l5 3.5L10 2" stroke="#fff" fill="none"/></svg>info@coastlinespinejoint.com</li>
      <li><svg viewBox="0 0 10 10"><circle cx="5" cy="5" r="4.5" fill="#9bcb3c"/></svg>www.coastlinespinejoint.com</li>
    </ul>
    <svg class="swoop" viewBox="0 0 300 110" preserveAspectRatio="none" aria-hidden="true">
      <path d="M0 110 Q80 20 300 0 L300 6 Q90 30 0 110z" fill="#3c3c3c"/>
      <path d="M0 110 Q90 34 300 10 L300 110z" fill="#9bcb3c"/>
    </svg>
  </article>

  <article class="panel" style="background:linear-gradient(#f2f2f2,#e2e2e2)">
    <div class="brand brand--cover"><i class="brand__dot"></i>Coastline Spine &amp; Joint</div>
    <div class="photo--patient" role="img" aria-label="Photo of an older man in a pink shirt holding his sore shoulder"></div>
    <svg class="cover-band" viewBox="0 0 300 160" preserveAspectRatio="none" aria-hidden="true">
      <path d="M0 22 Q150 0 300 4 L300 160 L0 160z" fill="#3c3c3c"/>
      <path d="M0 30 Q150 8 300 12 L300 160 L0 160z" fill="#9bcb3c"/>
    </svg>
    <p class="cover-title">FORMERLY HALDEN<br>FAMILY CHIROPRACTIC</p>
    <p class="cover-url">www.coastlinespinejoint.com</p>
  </article>
</section>

<section class="spread spread--inside">
  <article class="panel">
    <h2 class="heading" style="margin-bottom:14px">Regenerative Medicine Q &amp; A<br>What is regenerative medicine?</h2>
    <p class="body-copy">Regenerative medicine is a form of biotechnology that involves injecting regenerative medicine products into injured tissues to help your body repair damage. Regenerative medicine uses tissue engineering techniques to repair muscles, ligaments, cartilage, and tendons damaged by injuries, overuse, and osteoarthritis. The medical providers at Coastline Spine &amp; Joint select from a variety of available treatments and products. These include amniotic allografts, hyaluronic acid, regenerative cells, and cytokines which are powerful growth factors that may help regenerate your own body's tissues.</p>
    <p class="body-copy">After you're injection with the amniotic allograft serum, the growth factors trigger repair at the site of injection. Over the course of the next several weeks, cells grow and multiply forming new tissue.</p>
    <div class="photo photo--hands" role="img" aria-label="Photo of hands giving a therapeutic back massage"></div>
  </article>

  <article class="panel panel--areas">
    <p class="areas-intro">Regenerative medicine may be used in the following areas:</p>
    <div class="figure" role="img" aria-label="Illustration of a running figure with marked joints"></div>
    <span class="area-label" style="top:70px;--len:110px">Shoulder</span>
    <span class="area-label" style="top:105px;--len:120px">Wrist</span>
    <span class="area-label" style="top:128px;--len:120px">Elbow</span>
    <span class="area-label" style="top:185px;--len:90px">Hip</span>
    <span class="area-label" style="top:240px;--len:90px">Ankle</span>
    <span class="area-label" style="top:270px;--len:80px">Knee</span>
    <div class="areas-copy">
      <p class="body-copy">There are many additional types of bone and soft tissue problems, including arthritis, that these injections may benefit.</p>
      <p class="body-copy">With regenerative medicine and amniotic allograft treatments, the team supports the natural healing abilities of your body without the need for drugs or surgical repair and painful recovery. However, not all forms of regenerative medicine are equal. At Coastline Spine &amp; Joint, the team only works with the best regenerative medicine labs to ensure that the right kind of products are selected and that they are of the best quality and highest safety.</p>
    </div>
  </article>

  <article class="panel">
    <h2 class="heading">How does regenerative medicine work?</h2>
    <p class="body-copy">The team uses lab-grade products that are sterilized and processed to inject into the injured area. Once injected, it is thought that these powerful products differentiate into a variety of tissues to trigger your own body to repair damaged tissues. This damage may involve minor tears in muscles, ligaments, and tendons, or cartilage and meniscus breakdown in joints.</p>
    <p class="body-copy">Regenerative medicine products contain the basic building blocks of the body tissues — including proteins, amino acids, and cytokines — responsible for healing and tissue growth. They also provide anti-inflammatory benefits by promoting repair of tissues affected by inflammation.</p>
    <p class="body-copy">While some inflammation is normal and has a benefit to healing injuries, long-term inflammation causes pain, swelling, and further damage to tissues. When you experience too much inflammation, it does more harm than good. Instead of constantly relying on anti-inflammatory medications, regenerative products may be able to correct the problem at the source and reduce the production of natural inflammatory chemicals so you can heal.</p>
    <div class="photo photo--back" role="img" aria-label="Photo of a woman at a desk holding her painful lower back"></div>
  </article>
</section>

</body>
</html>
```